Vinyl Banner for bike shop to hang outside a railway station and attract new customers)

We run a small indenendent bike shop on the main campus at Halvercombe Institute.

Just up the road from us is the Halvercombe train station where thousands of commuters enter and exit each day.

We have permssion to hang a vinyl banner 1.2m x 3.5m directly opposite the ttrain station entrance/exit.

Vinyl Banner adverts must:
Clearly display Pondel Wheels logo
Include directional arrows pointing left.
List our email, url and phone details
Promote the purchasing of new bikes through Ridepathplan
Promote Bike Hire
Promote repairs and servicing of all bikes.
Promote sales of accesories including and especially Vornastel D locks
Be friendly to a female target audience without excluding men.
Be in keeping with our logo font etc.
Be a significant impovemnet on our current banner
Include logo's of our major brands (Tavoli Bikes, Palmwick Bikes, Oskel Bikes, Vush Bikes, Lappet Bikes, Quill Bikes)

Include "10% OFF for all PCW Staff'

I've added some image files you may or may not wish to use. All of which are currently used somewhere on our website.

Target Market(s)

Commuters, Students,

Industry/Entity Type

Shop

Requirements
Must have
• Our logo and brand logo's
Nice to have
• We generally use Exo font
Should not have
• Clip art!!!!

```html
<!DOCTYPE html>
<html lang="en">
<head>
<meta charset="utf-8">
<title>Pondel Wheels – Station Banner</title>
<link rel="stylesheet" href="https://fonts.googleapis.com/css2?family=Exo+2:ital,wght@0,300;0,400;0,600;0,800;1,300&family=Saira+Condensed:wght@700;800&display=swap">
<style>
  :root {
    --backdrop: #5d5e63;
    --paper: #f6f4f1;
    --plum: #3e1840;
    --plum-band: #582455;
    --magenta: #e8177f;
    --ink: #1d1b1c;
    --white: #ffffff;
  }
  * { box-sizing: border-box; margin: 0; padding: 0; }
  html, body { width: 1200px; height: 1000px; overflow: hidden; }
  body {
    background: var(--backdrop);
    font-family: "Exo 2", sans-serif;
    position: relative;
  }
  .banner {
    position: absolute;
    left: 32px; top: 313px;
    width: 1136px; height: 390px;
    background: var(--paper);
    overflow: hidden;
  }
  .skyline-art {
    position: absolute;
    left: 0; top: 30px;
    width: 620px; height: 300px;
    background:
      radial-gradient(ellipse 45% 55% at 60% 40%, rgba(238,140,199,.85), transparent 70%),
      radial-gradient(ellipse 40% 50% at 25% 60%, rgba(154,120,182,.8), transparent 72%),
      radial-gradient(ellipse 35% 45% at 75% 70%, rgba(94,40,90,.75), transparent 70%),
      radial-gradient(ellipse 30% 30% at 55% 88%, rgba(232,23,127,.7), transparent 75%);
  }
  .brand-row {
    position: absolute;
    right: 28px; top: 22px;
    display: flex; gap: 22px; align-items: center;
    font-weight: 600; font-size: 15px; color: var(--ink);
    letter-spacing: .5px; white-space: nowrap;
  }
  .headline {
    position: absolute;
    left: 526px; top: 60px;
    font-family: "Saira Condensed", "Exo 2", sans-serif;
    font-weight: 800; font-size: 58px; line-height: 1;
    color: var(--plum); white-space: nowrap;
  }
  .services {
    position: absolute;
    left: 655px; top: 126px;
    list-style: none;
    color: var(--plum);
    font-family: "Saira Condensed", "Exo 2", sans-serif;
    white-space: nowrap;
  }
  .services li {
    font-weight: 700; font-size: 38px; line-height: 45px;
  }
  .services li::before { content: "· "; }
  .services .note {
    font-family: "Exo 2", sans-serif;
    font-weight: 400; font-size: 14px; line-height: 16px;
    padding-left: 22px;
  }
  .services .note::before { content: ""; }
  .scheme {
    position: absolute;
    left: 884px; top: 146px; width: 216px;
    text-align: center; color: var(--plum);
    white-space: nowrap;
  }
  .scheme-lead { font-weight: 300; font-style: italic; font-size: 18px; }
  .scheme-mark {
    width: 70px; height: 70px; margin: 6px auto 0;
    background: var(--plum-band); border-radius: 10px;
  }
  .scheme-name {
    margin-top: 2px;
    font-family: "Saira Condensed", "Exo 2", sans-serif;
    font-weight: 800; font-size: 27px; line-height: 1.2;
  }
  .wayfinder { position: absolute; left: 0; top: 0; }
  .logo-badge {
    position: absolute;
    left: 78px; top: 25px;
    width: 220px; height: 220px; border-radius: 50%;
    background: var(--ink); border: 5px solid var(--paper);
    display: flex; flex-direction: column; justify-content: center; align-items: center;
    color: var(--white); font-weight: 400; font-size: 40px; line-height: 1.05;
    letter-spacing: 1px;
  }
  .location {
    position: absolute;
    left: 30px; top: 262px; width: 200px;
    text-align: center; color: var(--plum); line-height: 1.1;
    white-space: nowrap;
  }
  .location .lead { font-size: 11px; font-weight: 600; }
  .location .place { font-size: 16px; font-weight: 600; }
  .location .detail { font-size: 11px; font-style: italic; font-weight: 300; }
  .contact-band {
    position: absolute;
    left: 0; bottom: 0; width: 100%; height: 62px;
    background: var(--plum-band);
    display: flex; align-items: center; gap: 34px;
    padding-left: 138px;
    color: var(--white); font-weight: 300; font-size: 27px;
    white-space: nowrap;
  }
  .contact-band span { display: flex; align-items: center; gap: 8px; }
  .contact-band svg { flex: none; }
</style>
</head>
<body>
  <main class="banner">
    <div class="skyline-art" role="img" aria-label="Watercolour city skyline in purple and pink with a line of cyclists riding along the bottom"></div>

    <div class="brand-row">
      <span>Lappet Bikes</span>
      <span>Quill</span>
      <span>Oskel Bikes</span>
      <span>Tavoli</span>
      <span>Vush</span>
      <span>Palmwick</span>
    </div>

    <h1 class="headline">PONDEL WHEELS PROVIDES</h1>

    <ul class="services">
      <li>Servicing</li>
      <li>Repairs</li>
      <li>Bike Hire</li>
      <li>Accessories</li>
      <li class="note">(including Vornastel D locks)</li>
    </ul>

    <div class="scheme">
      <p class="scheme-lead">Save at least 25% with</p>
      <div class="scheme-mark"></div>
      <p class="scheme-name">ridepathplan.co.uk</p>
    </div>

    <svg class="wayfinder" width="340" height="390" viewBox="0 0 340 390" aria-hidden="true">
      <path d="M16 292 L92 228 L92 250 L230 250 Q300 250 300 190 L300 180 L320 180 L320 200 Q320 336 230 336 L92 336 L92 358 Z"
            fill="var(--magenta)"/>
      <path d="M28 292 L88 242 L88 262 L230 262 Q290 262 292 196 L308 196 Q306 324 230 324 L88 324 L88 344 Z"
            fill="var(--paper)" opacity=".9"/>
    </svg>

    <div class="logo-badge"><span>PONDEL</span><span>WHEELS</span></div>

    <div class="location">
      <p class="lead">We're at the</p>
      <p class="place">Halvercombe Institute</p>
      <p class="detail">(next to Porter Hall, R12)</p>
    </div>

    <footer class="contact-band">
      <span>
        <svg width="28" height="28" viewBox="0 0 28 28" fill="none" stroke="currentColor" stroke-width="2">
          <circle cx="14" cy="14" r="12"/><ellipse cx="14" cy="14" rx="5" ry="12"/><path d="M2 14h24M4 8h20M4 20h20"/>
        </svg>PondelWheels.org.uk</span>
      <span>
        <svg width="30" height="22" viewBox="0 0 30 22" fill="none" stroke="currentColor" stroke-width="2">
          <rect x="1" y="1" width="28" height="20"/><path d="M1 1l14 11L29 1"/>
        </svg>info@pondelwheels.org.uk</span>
      <span>
        <svg width="18" height="30" viewBox="0 0 18 30" fill="none" stroke="currentColor" stroke-width="2">
          <rect x="1" y="1" width="16" height="28" rx="3"/><path d="M7 25h4"/>
        </svg>0800 555 0142</span>
    </footer>
  </main>
</body>
</html>
```